Business Card Design Project

I want my business cards to stand and feel timeless! I also want people to get their hands on them and freak out over how cool these are, I already have a logo i just want a very cool card design! this is for a makeup artist and maybe one day a line of cosmetics.

Target Market(s)

I want this to target women from 18 to 45

Industry/Entity Type

Business

Font styles to use
Decorative
Script

Colors

Designer to choose colors to be used in the design.

Requirements
Must have
• it must be elegante

```html
<!DOCTYPE html>
<html lang="en">
<head>
<meta charset="utf-8">
<title>Clara Voss Makeup – Business Card</title>
<link rel="stylesheet" href="https://fonts.googleapis.com/css2?family=Oswald:wght@300;500&display=swap">
<style>
  :root {
    --page-bg: #2b2b2c;
    --card-bg: #151515;
    --gold: #9a7a1c;
    --ink-white: #f4f4f4;
  }
  * { margin: 0; padding: 0; box-sizing: border-box; }
  html, body {
    width: 1200px;
    height: 1000px;
    overflow: hidden;
    background: var(--page-bg);
  }
  .canvas {
    position: relative;
    width: 1200px;
    height: 1000px;
  }
  .business-card {
    position: absolute;
    left: 150px;
    top: 240px;
    width: 900px;
    height: 520px;
    background: var(--card-bg);
    border-radius: 4px;
    box-shadow: 0 20px 50px rgba(0,0,0,0.45);
    overflow: hidden;
  }
  .card-lines {
    position: absolute;
    inset: 0;
  }
  .brand-name {
    position: absolute;
    left: 160px;
    top: 168px;
    font-family: "Oswald", sans-serif;
    font-weight: 300;
    font-size: 100px;
    line-height: 1;
    letter-spacing: 6px;
    color: var(--ink-white);
    white-space: nowrap;
  }
  .contact-row {
    position: absolute;
    left: 140px;
    right: 40px;
    top: 338px;
    display: flex;
    align-items: center;
    gap: 7px;
    font-family: "Oswald", sans-serif;
    font-size: 17px;
    letter-spacing: 1.2px;
    white-space: nowrap;
  }
  .contact-label {
    color: var(--gold);
    font-weight: 500;
    text-transform: uppercase;
  }
  .contact-value {
    color: var(--ink-white);
    font-weight: 500;
    font-size: 13px;
    letter-spacing: 1.6px;
    margin-right: 8px;
  }
  .contact-value:last-child { margin-right: 0; }
  .contact-dot {
    width: 12px;
    height: 12px;
    border-radius: 50%;
    background: var(--gold);
    flex: none;
  }
</style>
</head>
<body>
  <main class="canvas">
    <section class="business-card">
      <svg class="card-lines" width="900" height="520" viewBox="0 0 900 520">
        <defs>
          <linearGradient id="fade-left" gradientUnits="userSpaceOnUse" x1="30" y1="0" x2="150" y2="0">
            <stop offset="0" stop-color="#9a7a1c" stop-opacity="0"/>
            <stop offset="1" stop-color="#9a7a1c"/>
          </linearGradient>
          <linearGradient id="fade-right-short" gradientUnits="userSpaceOnUse" x1="780" y1="0" x2="870" y2="0">
            <stop offset="0" stop-color="#9a7a1c"/>
            <stop offset="1" stop-color="#9a7a1c" stop-opacity="0"/>
          </linearGradient>
          <linearGradient id="fade-right-long" gradientUnits="userSpaceOnUse" x1="172" y1="0" x2="880" y2="0">
            <stop offset="0.75" stop-color="#9a7a1c"/>
            <stop offset="1" stop-color="#9a7a1c" stop-opacity="0"/>
          </linearGradient>
        </defs>
        <polyline points="430,160 780,160 780,252" fill="none" stroke="#9a7a1c" stroke-width="2"/>
        <line x1="780" y1="252" x2="870" y2="252" stroke="url(#fade-right-short)" stroke-width="2"/>
        <line x1="30" y1="252" x2="150" y2="252" stroke="url(#fade-left)" stroke-width="2"/>
        <line x1="172" y1="318" x2="880" y2="318" stroke="url(#fade-right-long)" stroke-width="2"/>
        <rect x="140" y="311" width="26" height="14" rx="2" fill="#9a7a1c" role="img" aria-label="Small gold mascara wand icon"/>
      </svg>

      <h1 class="brand-name">CLARA VOSS</h1>

      <div class="contact-row">
        <span class="contact-label">Website</span>
        <span class="contact-dot"></span>
        <span class="contact-value">WWW.CVMAKEUP.COM</span>
        <span class="contact-label">Email</span>
        <span class="contact-dot"></span>
        <span class="contact-value">INFO@CVMAKEUP.COM</span>
        <span class="contact-label">Telephone</span>
        <span class="contact-dot"></span>
        <span class="contact-value">000 000 000 0</span>
      </div>
    </section>
  </main>
</body>
</html>
```